Redesign my business cards

I would like pretty much all the same information as my current business cards but redesigned to stand out more and be more unique photo uploaded to show my current business cards don’t mind if you want to remove or replace I for on the back

```html
<!DOCTYPE html>
<html lang="en">
<head>
<meta charset="utf-8">
<title>Halvane Detailing – Business Cards</title>
<link href="https://fonts.googleapis.com/css2?family=Montserrat:wght@400;500;700;800&display=swap" rel="stylesheet">
<style>
  :root{
    --stage:#7a7a7a;
    --card-blue:#2b5188;
    --accent-red:#f25a5c;
    --text-white:#ffffff;
    --text-muted:#8fa3c4;
    --name-blue:#8fd6f5;
  }
  *{box-sizing:border-box;margin:0;padding:0}
  html,body{width:1200px;height:800px;overflow:hidden}
  body{
    background:var(--stage);
    font-family:"Montserrat",sans-serif;
    position:relative;
  }
  .card{
    position:absolute;
    left:285px;
    width:630px;height:360px;
    background:var(--card-blue);
    overflow:hidden;
    box-shadow:0 10px 24px rgba(0,0,0,.28);
  }
  .card--services{top:24px}
  .card--contact{top:412px}
  .card__waves{position:absolute;inset:0;width:100%;height:100%}

  /* Services side */
  .service-list{position:absolute;left:30px;top:26px;width:360px}
  .service{margin-bottom:14px}
  .service__title{
    color:var(--text-white);font-weight:800;font-size:24px;
    letter-spacing:.5px;line-height:1.1;white-space:nowrap;
  }
  .service__detail{
    color:var(--text-muted);font-size:11.5px;font-weight:500;
    line-height:1.35;margin-top:3px;letter-spacing:.3px;
  }
  .price{
    position:absolute;
    color:var(--text-white);font-weight:800;font-size:30px;line-height:1;
  }
  .price__sign{color:var(--accent-red)}
  .price--interior{top:70px;left:500px}
  .price--exterior{top:160px;left:455px}
  .price--full{top:250px;left:410px}

  /* Contact side */
  .wash-art{
    position:absolute;left:0;bottom:0;width:200px;height:210px;
    background:radial-gradient(ellipse at 30% 55%, #f4f8fc 0%, #bcdcf5 40%, rgba(120,180,235,.5) 65%, rgba(43,81,136,0) 80%);
  }
  .contact-list{position:absolute;left:92px;top:28px;list-style:none}
  .contact-item{display:flex;align-items:center;gap:12px;color:var(--text-white)}
  .contact-item + .contact-item{margin-top:8px}
  .contact-icon{
    width:30px;height:30px;border-radius:50%;
    background:var(--accent-red);display:flex;align-items:center;justify-content:center;
    flex-shrink:0;
  }
  .contact-item--phone{font-weight:800;font-size:26px;letter-spacing:1px}
  .contact-item--email{font-weight:500;font-size:17px;letter-spacing:1px}
  .owner-name{
    position:absolute;right:40px;bottom:80px;
    color:var(--name-blue);font-weight:700;font-size:19px;letter-spacing:1.5px;
  }
  .brand-name{
    position:absolute;left:150px;bottom:26px;
    color:var(--text-white);font-weight:800;font-size:34px;letter-spacing:-.3px;
    white-space:nowrap;
  }
</style>
</head>
<body>

<section class="card card--services" aria-label="Services and prices">
  <svg class="card__waves" viewBox="0 0 630 360" preserveAspectRatio="none" aria-hidden="true">
    <defs>
      <linearGradient id="svc-light" x1="0" y1="1" x2="0.4" y2="0">
        <stop offset="0" stop-color="#ffffff"/>
        <stop offset="1" stop-color="#5cc3f2"/>
      </linearGradient>
      <linearGradient id="svc-violet" x1="0" y1="0" x2="1" y2="1">
        <stop offset="0" stop-color="#6b7ff2"/>
        <stop offset="1" stop-color="#3c6fd8"/>
      </linearGradient>
    </defs>
    <path d="M630 150 C585 160 545 200 540 255 C535 310 520 340 480 360 L630 360 Z" fill="url(#svc-light)"/>
    <path d="M630 175 C600 190 580 220 585 270 C590 320 590 345 570 360 L630 360 Z" fill="url(#svc-violet)" stroke="#24477c" stroke-width="5"/>
  </svg>

  <div class="service-list">
    <div class="service">
      <h2 class="service__title">INTERIOR DETAIL</h2>
      <p class="service__detail">vacuum &amp; deep clean of carpets &amp; upholstery or leather treatment · interior trim clean &amp; condition · window polish and treatment · steam clean and stain removal</p>
    </div>
    <div class="service">
      <h2 class="service__title">EXTERIOR DETAIL</h2>
      <p class="service__detail">extreme wash &amp; polish · exterior trim reviver &amp; protector · window polish &amp; treatment · tyre dressing · engine bay cleaning</p>
    </div>
    <div class="service">
      <h2 class="service__title">FULL EXTREME DETAIL</h2>
      <p class="service__detail">extreme wash &amp; polish · tyre dressing · engine bay cleaned · vacuum &amp; deep clean of carpets &amp; upholstery or leather treatment · interior &amp; exterior trim reviver &amp; protector · window polish and treatment</p>
    </div>
  </div>

  <p class="price price--interior"><span class="price__sign">$</span>150</p>
  <p class="price price--exterior"><span class="price__sign">$</span>250</p>
  <p class="price price--full"><span class="price__sign">$</span>350</p>
</section>

<section class="card card--contact" aria-label="Contact details">
  <svg class="card__waves" viewBox="0 0 630 360" preserveAspectRatio="none" aria-hidden="true">
    <defs>
      <linearGradient id="ct-violet" x1="0" y1="0" x2="0" y2="1">
        <stop offset="0" stop-color="#d8d8f2"/>
        <stop offset="0.5" stop-color="#7c86dc"/>
        <stop offset="1" stop-color="#3a3fcf"/>
      </linearGradient>
      <linearGradient id="ct-light" x1="0" y1="0" x2="1" y2="0.6">
        <stop offset="0" stop-color="#ffffff"/>
        <stop offset="0.5" stop-color="#e9f4fb"/>
        <stop offset="1" stop-color="#4aa3dc"/>
      </linearGradient>
    </defs>
    <path d="M630 40 C560 70 480 100 450 170 C425 235 470 300 440 360 L630 360 Z" fill="url(#ct-violet)"/>
    <path d="M630 55 C575 80 530 120 515 180 C500 245 540 310 520 360 L630 360 Z" fill="url(#ct-light)" stroke="#24477c" stroke-width="5"/>
  </svg>

  <div class="wash-art" role="img" aria-label="Illustration of a car being washed with soap bubbles"></div>

  <ul class="contact-list">
    <li class="contact-item contact-item--phone">
      <span class="contact-icon">
        <svg width="16" height="16" viewBox="0 0 24 24" aria-hidden="true"><path fill="#fff" d="M6.6 10.8a15.2 15.2 0 0 0 6.6 6.6l2.2-2.2c.3-.3.7-.4 1-.2 1.1.4 2.3.6 3.6.6.6 0 1 .4 1 1V20c0 .6-.4 1-1 1A17 17 0 0 1 3 4c0-.6.4-1 1-1h3.5c.6 0 1 .4 1 1 0 1.3.2 2.5.6 3.6.1.3 0 .7-.2 1z"/></svg>
      </span>
      0412557031
    </li>
    <li class="contact-item contact-item--email">
      <span class="contact-icon">
        <svg width="16" height="16" viewBox="0 0 24 24" aria-hidden="true"><rect x="3" y="6" width="18" height="12" rx="1.5" fill="none" stroke="#fff" stroke-width="2"/><path d="M3.5 7l8.5 6 8.5-6" fill="none" stroke="#fff" stroke-width="2"/></svg>
      </span>
      HELLO@HALVANEDETAILING.COM
    </li>
  </ul>

  <p class="owner-name">OWEN TARRANT</p>
  <p class="brand-name">HALVANE DETAILING</p>
</section>

</body>
</html>
```